Real Estate Entrepreneur needs a business card

I am a real estate entrepreneur, I buy houses for investment purposes, I act as a real estate agent representing buyers and sellers in residential home transactions, I am a contractor that does a wide range of home repairs and construction. I'd like a design that can stick with me through the years as my business grows and morphs to fit any niche I decide to pursue as markets change.

Target Market(s)

Anyone with interest that may be related to real estate.

Industry/Entity Type

Real Estate

Contact Information for Business Card

A card that stands out and doesn't put me in any one box. My business will evolve over time and I need a card that can stay relevant.

Colors

Designer to choose colors to be used in the design.

Requirements
Must have
• Character
Nice to have
• I'm open
Should not have
• Cliche houses and hammers

```html
<!DOCTYPE html>
<html lang="en">
<head>
<meta charset="utf-8">
<title>Reid Calder – Business Card</title>
<link rel="stylesheet" href="https://fonts.googleapis.com/css2?family=Roboto:wght@400;500;700;900&display=swap">
<style>
  :root {
    --page-bg: #3a3f47;
    --card-black: #161616;
    --card-black-edge: #202020;
    --accent-red: #e3222b;
    --text-white: #f2f2f2;
    --text-soft: #d4d4d4;
    --rule: #8a7f74;
    --metal-light: #e6e6e6;
    --metal-mid: #b9b9b9;
    --metal-dark: #8e8e8e;
    --text-dark: #1a1a1a;
  }
  * { margin: 0; padding: 0; box-sizing: border-box; }
  html, body { width: 1200px; height: 900px; overflow: hidden; }
  body {
    background: var(--page-bg);
    font-family: "Roboto", Arial, sans-serif;
    display: flex;
    align-items: center;
    justify-content: center;
    gap: 40px;
  }
  .card {
    width: 520px;
    height: 297px;
    position: relative;
    box-shadow: 0 12px 28px rgba(0,0,0,.45);
  }
  /* Front */
  .card-front {
    background: linear-gradient(160deg, var(--card-black-edge), var(--card-black));
    color: var(--text-white);
    padding: 44px 40px 34px;
  }
  .brand-name {
    font-weight: 900;
    font-size: 36px;
    letter-spacing: 1px;
    line-height: 1;
    color: var(--accent-red);
  }
  .brand-title {
    font-size: 14px;
    letter-spacing: 1px;
    margin-top: 6px;
    color: var(--text-white);
  }
  .divider {
    height: 1px;
    background: var(--rule);
    margin-top: 12px;
    width: 440px;
  }
  .contact-list {
    list-style: none;
    margin-top: 18px;
    font-size: 13px;
    color: var(--text-soft);
  }
  .contact-list li {
    display: flex;
    align-items: center;
    gap: 10px;
    margin-bottom: 8px;
  }
  .contact-list svg { width: 13px; height: 13px; fill: var(--accent-red); }
  .address {
    position: absolute;
    right: 40px;
    bottom: 34px;
    font-size: 14px;
    line-height: 1.45;
    color: var(--text-soft);
    text-align: left;
  }
  /* Back */
  .card-back {
    background: linear-gradient(120deg, var(--metal-dark) 0%, var(--metal-light) 30%, var(--metal-mid) 50%, var(--metal-light) 70%, var(--metal-dark) 100%);
    color: var(--text-dark);
  }
  .back-name {
    position: absolute;
    top: 80px;
    left: 0;
    width: 100%;
    text-align: center;
    font-weight: 900;
    font-size: 40px;
    letter-spacing: 1px;
    color: var(--accent-red);
  }
  .services {
    position: absolute;
    top: 160px;
    left: 0;
    width: 100%;
    text-align: center;
    list-style: none;
    font-weight: 700;
    font-size: 11.5px;
    letter-spacing: .6px;
    line-height: 1.6;
    text-transform: uppercase;
  }
</style>
</head>
<body>
  <section class="card card-front">
    <div class="brand-name">REID CALDER</div>
    <div class="brand-title">REAL ESTATE ENTREPRENEUR</div>
    <div class="divider"></div>
    <ul class="contact-list">
      <li>
        <svg viewBox="0 0 24 24" aria-hidden="true"><path d="M6.6 10.8a15.1 15.1 0 0 0 6.6 6.6l2.2-2.2a1 1 0 0 1 1-.25 11.4 11.4 0 0 0 3.6.57 1 1 0 0 1 1 1V20a1 1 0 0 1-1 1A17 17 0 0 1 3 4a1 1 0 0 1 1-1h3.5a1 1 0 0 1 1 1c0 1.25.2 2.45.57 3.57a1 1 0 0 1-.25 1z"/></svg>
        (555) 014-2290
      </li>
      <li>
        <svg viewBox="0 0 24 24" aria-hidden="true"><path d="M2 4h20v16H2z M4 6.5v.2l8 5.3 8-5.3v-.2z" fill-rule="evenodd"/></svg>
        info@reidcalder.com
      </li>
    </ul>
    <address class="address" style="font-style:normal">
      880, 412 Harbour Street W<br>
      Brookfield, AB, T0X 4K2
    </address>
  </section>

  <section class="card card-back">
    <div class="back-name">REID CALDER</div>
    <ul class="services">
      <li>Buy houses for investment purposes</li>
      <li>Representing buyers and sellers in residential home transactions</li>
      <li>Wide range of home repairs and construction</li>
    </ul>
  </section>
</body>
</html>
```